Manuka honey jar label for new Manuka brand

We are planning to start a Manuka honey brand and we need to design the label for the honey jar. Manuka honey is an up and coming product and the market is still young in our country.
Our market is dominated by 1 brand: Orvana Health (photo attached). To the people who know what Manuka honey is, they associate it with Orvana Health in the same way people associate Cola with Zindle Pop or printer copies with Quorvix.
The good news is that a lot of people do not know yet what Manuka honey is and we still have the opportunity of being the first brand they get to know. At the same time, we still need to be able to take at least a bite out of the Orvana Health market share.
The Orvana Health label for their jar I think is not just absolutely gorgeous but it also does its job extremely well. It only features 3 informations:
- name of brand/logo (Orvana Health)
- name of product (Manuka Honey)
- and mgo rating which is like a rating of how strong the honey is
By having just this information on a relatively small label, their label SCREAMS Manuka by having the Manuka words twice (the brand and the product name) and people develop this association between Orvana Health and Manuka products in general.
Our product will also be in a similar square plastic jar. It will also be dark tinted, that´s important to note. We can also go for a blue cap but in order to differentiate ourselves from Orvana Health we thought of maybe choosing a black lid instead. I uploaded 2 jars, 1 with black lid and 1 with gold (although it looks more like mustard) that you can use for simulations. They are pretty accurate of the type of jars and lids that we can have.
The label has total length of about 20cm. One side of the jar has 5,5 cm of the label and the height of the label is 4,5 cm. We can also use selective gold laminating on the label but we cannot have custom shape label at this point as Orvana Health does with its tree logo that sticks outside the label.
I need the design for the entire label but the focus should be on the front part, that is the part that sells and catches your eye. Like Orvana Health, the front part I want to have 3 vital informations:
- name of brand/logo (in our case Velmora Botanica) - we do not have a pre-existing logo, this needs to be created alongside the label
- and mgo rating
As "other" information we also need the net weight "250 g" alongside with the typical "e" to appear on the front. That is a legal requirement.
Optionally, you can add a small phrase somewhere like "Harvested in New Zealand" or "Made in New Zealand" since this is a product that is only made there and in some areas of Australia.
This is pretty much all the info. As a final note, there are a ton of beautiful premium Manuka honey jar labels. But they are too fancy and when you look at them you don´t instantly recognize that it is Manuka Honey.
This instant recognition is vital! With this small jar there is the danger for customers to think that maybe it´s medicine, maybe it´s sports supplements etc. This is a relatively small product and imagine you just glance on it on the retail shelf. Instantly you must think it is Manuka Honey and that it is beautiful. And if you see it on the shelf next to Orvana Health, it would be best to also think that you would rather buy this (it gives you more trust) than the Orvana Health.
One final note: I do not want the bee as an insect on the label. I think some people are turned off when they see an insect with its small legs and make a bad association that there are insects inside. I do not mind symbolism or somehow super stylized bee in a modern way, but I do not want a plain insect on the label.
For any other questions, I am at your disposal. Thank you very much for taking the time to send us a proposal!

```html
<!DOCTYPE html>
<html lang="en">
<head>
<meta charset="utf-8">
<title>Mānuka Honey Label – Velmora Botanica</title>
<link rel="stylesheet" href="https://fonts.googleapis.com/css2?family=Big+Shoulders+Display:wght@800;900&family=Oswald:wght@500;600&display=swap">
<style>
  :root {
    --bg: #ececec;
    --label: #ffffff;
    --teal: #1b5a6d;
    --teal-soft: #4f8ea3;
    --yellow: #f4d92c;
    --yellow-deep: #e9c91a;
  }
  html, body {
    margin: 0;
    padding: 0;
    width: 1200px;
    height: 1200px;
    overflow: hidden;
    background: var(--bg);
  }
  .canvas {
    position: relative;
    width: 1200px;
    height: 1200px;
  }
  .label {
    position: absolute;
    left: 50px;
    top: 151px;
    width: 1100px;
    height: 898px;
    background: var(--label);
    box-shadow: 0 2px 10px rgba(0,0,0,0.08);
  }
  .label svg { display: block; }
  .brand-name {
    font-family: "Oswald", sans-serif;
    font-weight: 600;
    fill: var(--teal);
  }
  .product-word {
    font-family: "Big Shoulders Display", sans-serif;
    font-weight: 900;
    fill: var(--teal);
  }
  .product-type {
    font-family: "Big Shoulders Display", sans-serif;
    font-weight: 900;
    fill: var(--yellow);
  }
  .origin {
    font-family: "Oswald", sans-serif;
    font-weight: 600;
    fill: var(--teal);
  }
  .badge-shape { fill: var(--yellow); }
  .badge-text {
    font-family: "Oswald", sans-serif;
    font-weight: 600;
    fill: var(--teal);
  }
</style>
</head>
<body>
<div class="canvas">
  <div class="label">
    <svg width="1100" height="898" viewBox="0 0 1100 898" xmlns="http://www.w3.org/2000/svg">
      <defs>
        <radialGradient id="mascotTones" cx="50%" cy="50%" r="55%">
          <stop offset="0%" stop-color="#f4d92c"/>
          <stop offset="55%" stop-color="#9cc3cf"/>
          <stop offset="100%" stop-color="#ffffff" stop-opacity="0"/>
        </radialGradient>
      </defs>

      <!-- brand mark -->
      <g class="brand">
        <circle cx="530" cy="110" r="22" fill="var(--yellow)"/>
        <text class="brand-name" x="530" y="160" font-size="17" text-anchor="middle">VELMORA</text>
        <text class="brand-name" x="530" y="181" font-size="17" text-anchor="middle">BOTANICA</text>
      </g>

      <!-- product word -->
      <text class="product-word" x="321" y="378" font-size="192" textLength="418" lengthAdjust="spacingAndGlyphs">MĀNUKA</text>

      <!-- mascot illustration area -->
      <rect x="418" y="224" width="238" height="269" rx="110" fill="url(#mascotTones)" role="img" aria-label="Stylised meditating bee mascot in teal and yellow"/>

      <!-- product type -->
      <text class="product-type" x="378" y="554" font-size="118" textLength="308" lengthAdjust="spacingAndGlyphs">HONEY</text>

      <!-- origin line -->
      <text class="origin" x="383" y="618" font-size="32" textLength="299" lengthAdjust="spacingAndGlyphs">Harvested in New Zeeland</text>

      <!-- MGO rating badge -->
      <g class="badge badge-mgo">
        <polygon class="badge-shape" points="170,691 341,691 361,724 341,757 170,757 150,724"/>
        <text class="badge-text" x="255" y="742" font-size="46" text-anchor="middle">MGO 250+</text>
      </g>

      <!-- net weight badge -->
      <g class="badge badge-weight">
        <polygon class="badge-shape" points="724,691 891,691 911,724 891,757 724,757 704,724"/>
        <text class="badge-text" x="807" y="742" font-size="46" text-anchor="middle">250 g ℮</text>
      </g>
    </svg>
  </div>
</div>
</body>
</html>
```